Business Card Design

Carl Benson Insurance Agency, an Independent Insurance Agency which was stated on Orchard Lane in Laplace, Louisiana on 1958 and has grown the six locations throughout South Louisiana. We sell personal (auto Homeowners flood, liability) and commercial insurance (commercial property, general liability, workers compensation, commercial auto). I am looking for a double sided card with list the five remaining locations on the back or maybe even a folded four sided card. Our home office is a two story building with a green roof. I have had a logo designed which I have attached. Open for revisions but would like to stay with in the same green roof over an M. I have attached the logo but can not tell if I was uploaded.

Target Market(s)

Individual and commercial insurance buyers. Upper income and business owners

Industry/Entity Type

Insurance

Requirements
Must have
• Must have similar logo as uploaded. Green roof over M or something similar. List all location address and phone numbers.

Employee name, office phone number; direct phone line; email address and website list all locations on card. Very Similar colors to current logo.
Nice to have
• Possible folded card with double sided print

```html
<!DOCTYPE html>
<html lang="en">
<head>
<meta charset="utf-8">
<title>Carl Benson Insurance Agency – Business Card</title>
<link href="https://fonts.googleapis.com/css2?family=Open+Sans:wght@400;600;700;800&display=swap" rel="stylesheet">
<style>
  :root {
    --page: #e9e6e1;
    --card-white: #ffffff;
    --brand-green: #1f6b4a;
    --brand-green-dark: #124a33;
    --brand-green-mid: #1c6446;
    --brand-blue: #1a6fc4;
    --ink-grey: #8a8a8a;
    --rule-grey: #c9c9c9;
    --white: #ffffff;
  }
  html, body {
    margin: 0;
    width: 1200px;
    height: 1023px;
    overflow: hidden;
    background: var(--page);
    font-family: "Open Sans", Arial, sans-serif;
  }
  .canvas { position: relative; width: 1200px; height: 1023px; }

  .card {
    position: absolute;
    width: 560px;
    height: 320px;
    box-sizing: border-box;
    box-shadow: 0 6px 18px rgba(0,0,0,0.18);
  }

  /* Front */
  .card-front {
    left: 60px; top: 150px;
    background: var(--card-white);
    padding: 34px 36px;
  }
  .brand { display: flex; align-items: center; gap: 12px; }
  .brand-square { width: 30px; height: 30px; background: var(--brand-green); }
  .brand-name {
    font-weight: 800; font-size: 22px; line-height: 1.05;
    color: var(--brand-green); text-transform: uppercase; letter-spacing: 0.3px;
  }
  .brand-tagline {
    margin: 6px 0 0 42px; font-size: 12px; font-weight: 700; color: var(--ink-grey);
  }
  .divider { height: 1px; background: var(--rule-grey); margin: 22px 0 18px; width: 300px; }
  .person-name {
    font-size: 22px; font-weight: 600; color: var(--brand-green);
    text-transform: uppercase; margin: 0; line-height: 1;
  }
  .person-title { font-size: 12px; color: var(--ink-grey); margin: 4px 0 12px; }
  .contact-list { list-style: none; margin: 0; padding: 0; font-size: 12px; color: var(--ink-grey); }
  .contact-list li { display: flex; align-items: center; gap: 8px; height: 18px; }
  .contact-icon { width: 12px; height: 12px; flex: none; }
  .address { font-size: 12px; color: var(--ink-grey); margin: 10px 0 0; line-height: 1.45; }
  .website { font-size: 12.5px; font-weight: 700; color: var(--brand-green); margin: 6px 0 0; }

  /* Back */
  .card-back {
    left: 580px; top: 560px;
    background: linear-gradient(160deg, var(--brand-green-mid) 0%, var(--brand-green-dark) 100%);
    padding: 26px 30px;
    color: var(--white);
  }
  .office-grid {
    display: grid; grid-template-columns: 1fr 1fr; column-gap: 26px; row-gap: 14px;
  }
  .office h3 { margin: 0 0 2px; font-size: 12px; font-weight: 700; }
  .office p { margin: 0; font-size: 11.5px; line-height: 1.45; }
  .office .phones { display: flex; align-items: center; gap: 5px; }
  .office .contact-icon { width: 11px; height: 11px; }
  .back-brand { position: absolute; right: 30px; bottom: 22px; text-align: left; }
  .back-brand .brand-square { background: var(--white); width: 22px; height: 22px; }
  .back-brand .brand-name { color: var(--white); font-size: 17px; }
  .back-brand .brand-tagline { color: var(--white); margin-left: 34px; font-size: 10px; }
</style>
</head>
<body>
<div class="canvas">

  <section class="card card-front">
    <div class="brand">
      <div class="brand-square"></div>
      <div class="brand-name">Carl Benson<br>Insurance Agency</div>
    </div>
    <p class="brand-tagline">Serving Orchard Lane Since 1958</p>
    <div class="divider"></div>
    <h1 class="person-name">Ryan Porter</h1>
    <p class="person-title">Director</p>
    <ul class="contact-list">
      <li><svg class="contact-icon" viewBox="0 0 12 12"><rect width="12" height="12" rx="2" fill="#1a6fc4"/><path d="M3.5 2.8l1.4 1.6-.7.9c.5 1 1.3 1.8 2.3 2.3l.9-.7 1.6 1.4-.9 1.1C5.8 9.2 2.8 6.2 2.6 3.7z" fill="#fff"/></svg>+1 985-310-4417</li>
      <li><svg class="contact-icon" viewBox="0 0 12 12"><rect width="12" height="12" rx="2" fill="#1a6fc4"/><rect x="3" y="5" width="6" height="4" fill="#fff"/><rect x="4" y="2.5" width="4" height="2.5" fill="#fff"/></svg>+1 985-310-4420</li>
      <li><svg class="contact-icon" viewBox="0 0 12 12"><rect width="12" height="12" rx="2" fill="#1a6fc4"/><rect x="2.5" y="3.5" width="7" height="5" fill="#fff"/><path d="M2.5 3.5l3.5 3 3.5-3" stroke="#1a6fc4" fill="none"/></svg>ryan@carlbenson.com</li>
    </ul>
    <p class="address">412 Cypress Ave., Ste. 110<br>Laplace Louisiana 70068-3321</p>
    <p class="website">www.bensonagency.com</p>
  </section>

  <section class="card card-back">
    <div class="office-grid">
      <div class="office">
        <h3>Main Office:</h3>
        <p>412 Cypress Ave., Ste. 110<br>Laplace Louisiana 70068-3321</p>
        <p class="phones"><svg class="contact-icon" viewBox="0 0 12 12"><rect width="12" height="12" rx="2" fill="#fff"/><path d="M3.5 2.8l1.4 1.6-.7.9c.5 1 1.3 1.8 2.3 2.3l.9-.7 1.6 1.4-.9 1.1C5.8 9.2 2.8 6.2 2.6 3.7z" fill="#1c6446"/></svg>0123 456 789 | <svg class="contact-icon" viewBox="0 0 12 12"><rect width="12" height="12" rx="2" fill="#fff"/><rect x="3" y="5" width="6" height="4" fill="#1c6446"/><rect x="4" y="2.5" width="4" height="2.5" fill="#1c6446"/></svg>0123 456 789</p>
      </div>
      <div class="office">
        <h3>Sub #1 Office:</h3>
        <p>412 Cypress Ave., Ste. 110<br>Laplace Louisiana 70068-3321</p>
        <p class="phones"><svg class="contact-icon" viewBox="0 0 12 12"><rect width="12" height="12" rx="2" fill="#fff"/><path d="M3.5 2.8l1.4 1.6-.7.9c.5 1 1.3 1.8 2.3 2.3l.9-.7 1.6 1.4-.9 1.1C5.8 9.2 2.8 6.2 2.6 3.7z" fill="#1c6446"/></svg>0123 456 789 | <svg class="contact-icon" viewBox="0 0 12 12"><rect width="12" height="12" rx="2" fill="#fff"/><rect x="3" y="5" width="6" height="4" fill="#1c6446"/><rect x="4" y="2.5" width="4" height="2.5" fill="#1c6446"/></svg>0123 456 789</p>
      </div>
      <div class="office">
        <h3>Sub#2 Office:</h3>
        <p>412 Cypress Ave., Ste. 110<br>Laplace Louisiana 70068-3321</p>
        <p class="phones"><svg class="contact-icon" viewBox="0 0 12 12"><rect width="12" height="12" rx="2" fill="#fff"/><path d="M3.5 2.8l1.4 1.6-.7.9c.5 1 1.3 1.8 2.3 2.3l.9-.7 1.6 1.4-.9 1.1C5.8 9.2 2.8 6.2 2.6 3.7z" fill="#1c6446"/></svg>0123 456 789 | <svg class="contact-icon" viewBox="0 0 12 12"><rect width="12" height="12" rx="2" fill="#fff"/><rect x="3" y="5" width="6" height="4" fill="#1c6446"/><rect x="4" y="2.5" width="4" height="2.5" fill="#1c6446"/></svg>0123 456 789</p>
      </div>
      <div class="office">
        <h3>Sub#3 Office:</h3>
        <p>412 Cypress Ave., Ste. 110<br>Laplace Louisiana 70068-3321</p>
        <p class="phones"><svg class="contact-icon" viewBox="0 0 12 12"><rect width="12" height="12" rx="2" fill="#fff"/><path d="M3.5 2.8l1.4 1.6-.7.9c.5 1 1.3 1.8 2.3 2.3l.9-.7 1.6 1.4-.9 1.1C5.8 9.2 2.8 6.2 2.6 3.7z" fill="#1c6446"/></svg>0123 456 789 | <svg class="contact-icon" viewBox="0 0 12 12"><rect width="12" height="12" rx="2" fill="#fff"/><rect x="3" y="5" width="6" height="4" fill="#1c6446"/><rect x="4" y="2.5" width="4" height="2.5" fill="#1c6446"/></svg>0123 456 789</p>
      </div>
      <div class="office">
        <h3>Sub#4 Office:</h3>
        <p>412 Cypress Ave., Ste. 110<br>Laplace Louisiana 70068-3321</p>
        <p class="phones"><svg class="contact-icon" viewBox="0 0 12 12"><rect width="12" height="12" rx="2" fill="#fff"/><path d="M3.5 2.8l1.4 1.6-.7.9c.5 1 1.3 1.8 2.3 2.3l.9-.7 1.6 1.4-.9 1.1C5.8 9.2 2.8 6.2 2.6 3.7z" fill="#1c6446"/></svg>0123 456 789 | <svg class="contact-icon" viewBox="0 0 12 12"><rect width="12" height="12" rx="2" fill="#fff"/><rect x="3" y="5" width="6" height="4" fill="#1c6446"/><rect x="4" y="2.5" width="4" height="2.5" fill="#1c6446"/></svg>0123 456 789</p>
      </div>
    </div>
    <div class="back-brand">
      <div class="brand">
        <div class="brand-square"></div>
        <div class="brand-name">Carl Benson<br>Insurance Agency</div>
      </div>
      <p class="brand-tagline">Serving Orchard Lane Since 1958</p>
    </div>
  </section>

</div>
</body>
</html>
```